NEED A BUSINESS CARD FOR A NEW ELECTRICAL BUSINESS

HI I am after a new business card for my new electrical business I have a logo that I have attached its the one in blue, I would like that on the front and on the back my name- Leonard Pike, Email leonardpike@tallmesh.com, mobile 0491362047, licence no# vic 47819, nsw 591304k I wont something that is a stand out from the rest but at the same time is neat as being a new business I wont it to catch peoples eye on the front of the card I would like the logo and not much else.
And on the back as well I would like a slogan saying something like
Quality-Reliable-Service

Hi all on the back of the card I would like a little slogan like Quality-Reliable-Service something like that would be good thanks

Hi all the business card needs to have both these licence numbers on it                                                  VIC-47819 nsw-591304k

```html
<!DOCTYPE html>
<html lang="en">
<head>
<meta charset="utf-8">
<title>Leonard Pike Electrical – Business Card</title>
<link href="https://fonts.googleapis.com/css2?family=Lato:wght@400;700;900&display=swap" rel="stylesheet">
<style>
  :root {
    --backdrop: #e9eaec;
    --card-black: #050505;
    --card-white: #ffffff;
    --brand-blue: #1565c0;
    --brand-blue-light: #1a86d0;
    --brand-blue-deep: #0d4f9e;
    --name-navy: #163f7a;
    --ink: #1c1c1c;
    --rule: #2a2a2a;
    --silver: #b8bcc2;
  }
  * { margin: 0; padding: 0; box-sizing: border-box; }
  html, body {
    width: 1200px; height: 926px; overflow: hidden;
    background: var(--backdrop);
    font-family: "Lato", Arial, sans-serif;
  }
  .sheet {
    width: 1200px; height: 926px;
    display: flex; flex-direction: column; align-items: center;
    justify-content: center; gap: 24px;
  }
  .card {
    position: relative; width: 700px; height: 427px; overflow: hidden;
    box-shadow: 0 4px 14px rgba(0,0,0,.18);
  }

  /* Front */
  .card--front { background: var(--card-black); }
  .card--front .band { position: absolute; inset: 0; width: 100%; height: 100%; }
  .brand {
    display: flex; align-items: center; gap: 14px;
    font-weight: 900; color: var(--brand-blue); text-transform: uppercase;
    letter-spacing: 2px; white-space: nowrap;
  }
  .brand__mark { background: var(--brand-blue); flex: none; }
  .card--front .brand {
    position: absolute; top: 118px; left: 0; right: 0; justify-content: center;
    font-size: 34px; color: var(--brand-blue-light);
  }
  .card--front .brand__mark { width: 30px; height: 30px; background: var(--brand-blue-light); }
  .slogan {
    position: absolute; left: 0; right: 0; top: 312px; text-align: center;
    color: #fff; font-size: 24px; font-weight: 700; letter-spacing: 5px;
    transform: rotate(2.2deg);
  }

  /* Back */
  .card--back { background: var(--card-white); }
  .card--back .brand {
    position: absolute; top: 160px; left: 34px;
    font-size: 19px; gap: 9px; letter-spacing: 1px;
  }
  .card--back .brand__mark { width: 20px; height: 20px; }
  .divider {
    position: absolute; left: 335px; top: 108px; width: 1.5px; height: 150px;
    background: var(--rule);
  }
  .contact { position: absolute; left: 365px; top: 110px; color: var(--ink); }
  .contact__name {
    font-size: 31px; font-weight: 400; color: var(--brand-blue); text-transform: uppercase;
    letter-spacing: .5px; margin-bottom: 16px;
  }
  .contact__name strong { font-weight: 700; color: var(--name-navy); }
  .contact__line { font-size: 19px; line-height: 24px; }
  .contact__line--gap { margin-top: 20px; }
  .contact__label { font-weight: 700; color: var(--brand-blue); }
  .base-band {
    position: absolute; left: 0; right: 0; bottom: 0; height: 44px;
    background: linear-gradient(180deg, var(--brand-blue-deep), var(--brand-blue-light));
  }
</style>
</head>
<body>
<main class="sheet">
  <section class="card card--front" aria-label="Card front">
    <svg class="band" viewBox="0 0 700 427" preserveAspectRatio="none" aria-hidden="true">
      <path d="M0 270 Q 350 250 700 330 L700 427 L0 427 Z" fill="var(--silver)"/>
      <path d="M0 276 Q 350 258 700 336 L700 427 L0 427 Z" fill="var(--brand-blue)"/>
    </svg>
    <div class="brand"><span class="brand__mark"></span>Leonard Pike Electrical</div>
    <p class="slogan">QUALITY - RELIABLE - SERVICE</p>
  </section>

  <section class="card card--back" aria-label="Card back">
    <div class="brand"><span class="brand__mark"></span>Leonard Pike Electrical</div>
    <div class="divider"></div>
    <div class="contact">
      <h1 class="contact__name">Leonard <strong>Pike</strong></h1>
      <p class="contact__line"><span class="contact__label">mobile:</span> 0491362047</p>
      <p class="contact__line"><span class="contact__label">email:</span> leonardpike@tallmesh.com</p>
      <p class="contact__line contact__line--gap"><span class="contact__label">licence no:</span> vic 47819, nsw 591304k</p>
    </div>
    <div class="base-band"></div>
  </section>
</main>
</body>
</html>
```